Vor Business Card

we need a business card for flooring business called Vor Flooring, the design should be black and white. we have 2 locations

Ashvale Showroom
274 Kellaway Road,
Ashvale VIC 3148

Carrowby Showroom
592 Tarrant Hwy,
Carrowby VIC 3207

email : sales@vorflooring.com.au
(03) 9517 2643

Please inform we sell , Laminate, Hybrid, Timber, carpet and commercial flooring

```html
<!DOCTYPE html>
<html lang="en">
<head>
<meta charset="utf-8">
<title>Vor Flooring – Business Card</title>
<link rel="stylesheet" href="https://fonts.googleapis.com/css2?family=Poppins:wght@300;400;500;600;700&display=swap">
<style>
  :root {
    --backdrop: #e6e7e8;
    --card-light: #ffffff;
    --card-dark: #1b1b1b;
    --ink: #141414;
    --ink-soft: #2a2a2a;
    --paper: #ffffff;
  }
  * { margin: 0; padding: 0; box-sizing: border-box; }
  html, body {
    width: 1200px; height: 900px; overflow: hidden;
    background: var(--backdrop);
    font-family: "Poppins", sans-serif;
  }
  .canvas { position: relative; width: 1200px; height: 900px; }
  .card { position: absolute; left: 280px; width: 640px; height: 366px; }
  .card-front { top: 60px; background: var(--card-light); color: var(--ink); }
  .card-back { top: 480px; background: var(--card-dark); color: var(--paper); }

  .person { position: absolute; left: 41px; top: 38px; }
  .person-name { font-weight: 700; font-size: 23px; letter-spacing: 0.3px; line-height: 1.1; }
  .person-role { font-weight: 400; font-size: 16px; line-height: 1.2; color: var(--ink-soft); }

  .brand-front {
    position: absolute; right: 45px; top: 132px;
    font-weight: 400; font-size: 28px; letter-spacing: 0.5px; color: var(--ink);
    white-space: nowrap;
  }

  .showrooms { position: absolute; left: 41px; top: 188px; }
  .showroom + .showroom { margin-top: 16px; }
  .showroom-title { font-weight: 500; font-size: 17px; line-height: 1.25; }
  .showroom-address { font-weight: 300; font-size: 16px; line-height: 1.35; color: var(--ink-soft); }

  .contact {
    position: absolute; left: 362px; top: 290px;
    font-weight: 300; font-size: 16px; line-height: 1.35; color: var(--ink-soft);
  }
  .contact-row { display: flex; align-items: center; gap: 5px; white-space: nowrap; }
  .contact-icon { width: 12px; height: 12px; flex: none; }

  .brand-back {
    position: absolute; left: 0; right: 0; top: 140px; text-align: center;
    font-weight: 400; font-size: 42px; letter-spacing: 0.5px; white-space: nowrap;
  }
  .services {
    position: absolute; left: 0; right: 0; top: 304px; text-align: center;
    font-weight: 500; font-size: 15px; letter-spacing: 0.3px; white-space: nowrap;
  }
</style>
</head>
<body>
<main class="canvas">
  <section class="card card-front">
    <div class="person">
      <div class="person-name">LIAM PORTER</div>
      <div class="person-role">Founder &amp; CEO</div>
    </div>

    <div class="brand-front">Vor Flooring</div>

    <div class="showrooms">
      <div class="showroom">
        <div class="showroom-title">Ashvale Showroom</div>
        <div class="showroom-address">274 Kellaway Road,<br>Ashvale VIC 3148</div>
      </div>
      <div class="showroom">
        <div class="showroom-title">Carrowby Showroom</div>
        <div class="showroom-address">592 Tarrant Hwy,<br>Carrowby VIC 3207</div>
      </div>
    </div>

    <div class="contact">
      <div class="contact-row">
        <svg class="contact-icon" viewBox="0 0 12 12" aria-hidden="true">
          <path d="M3 1 L4.6 3.4 L3.6 4.6 Q4.6 7 7.2 8.4 L8.4 7.4 L11 9 L10 11 Q4 10.6 1.2 2.2 Z" fill="var(--ink)"/>
        </svg>
        <span>(03) 9517 2643</span>
      </div>
      <div class="contact-row">
        <svg class="contact-icon" viewBox="0 0 12 12" aria-hidden="true">
          <rect x="0.8" y="2.3" width="10.4" height="7.4" fill="none" stroke="var(--ink)" stroke-width="1.2"/>
          <path d="M0.8 2.6 L6 6.6 L11.2 2.6" fill="none" stroke="var(--ink)" stroke-width="1.2"/>
        </svg>
        <span>sales@vorflooring.com.au</span>
      </div>
    </div>
  </section>

  <section class="card card-back">
    <div class="brand-back">Vor Flooring</div>
    <div class="services">Laminate | Hybrid | Timber | carpet and commercial flooring</div>
  </section>
</main>
</body>
</html>
```